Vorel constructions

We are predominantly a residential home builder based in Melbourne, Victoria Australia. We construct houses, apartments, townhouses, multi-unit developments.

The name of the company is "Vorel Constructions"
My company believes in building unique construction projects mainly residential homes. The target customers are upmarket Melbourne residents/investors.

I want the brand name "Vorel" to be part of the logo. There's no need to put the word construction in the logo at this stage.

I would also like some ideas for a slogan e.g. "Just build it." or "We build quality homes." But I would like something unique and different for a slogan not the same old cliche.

vorelconstructions.example.com.au
e: tmelo@vorelconstructions.example.com.au
M: 0417305862
Address: 8/3 Fenwick Lane Clayton VIC 3168

Director:Mr Dinesh Malarkodiyan

```html
<!DOCTYPE html>
<html lang="en">
<head>
<meta charset="utf-8">
<title>Vorel Constructions – Business Card</title>
<link href="https://fonts.googleapis.com/css2?family=Questrial&family=Didact+Gothic&display=swap" rel="stylesheet">
<style>
  :root {
    --page: #ffffff;
    --card-dark: #0b0c0d;
    --card-mid: #1d2124;
    --brand-cyan: #3ee8dc;
    --label-green: #5a7a68;
    --constructors-grey: #5f7567;
    --mint-text: #c8f0d8;
    --white: #ffffff;
    --web-yellow: #e6cf1e;
    --rule-olive: #5f5e34;
    --tape-yellow: #e8c81a;
    --tape-dark: #b8960c;
    --house-grey: #d8d8d4;
  }
  * { margin: 0; padding: 0; box-sizing: border-box; }
  html, body { width: 1200px; height: 1000px; overflow: hidden; background: var(--page); }
  .sheet { position: relative; width: 1200px; height: 1000px; font-family: "Questrial", sans-serif; }

  .card {
    position: absolute; left: 0; width: 942px; overflow: hidden;
    background: radial-gradient(ellipse at 50% 45%, var(--card-mid) 0%, var(--card-dark) 75%);
  }
  .card--front { top: 0; height: 495px; }
  .card--back { top: 502px; height: 498px; }

  .side-label {
    position: absolute; font-family: "Didact Gothic", sans-serif;
    color: var(--label-green); font-size: 46px; letter-spacing: 1px;
  }
  .side-label--front { left: 957px; top: 230px; }
  .side-label--back { left: 963px; top: 750px; }

  .brand-name {
    position: absolute; font-family: "Questrial", sans-serif;
    color: var(--brand-cyan); font-size: 150px; line-height: 1; letter-spacing: 4px;
  }
  .card--front .brand-name { left: 285px; top: 95px; }
  .card--back .brand-name { left: 305px; top: 60px; }

  .house-art {
    position: absolute; border-radius: 6px;
    background: linear-gradient(180deg, var(--house-grey), #b9b9b4);
  }
  .card--front .house-art { left: 668px; top: 103px; width: 160px; height: 90px; }
  .card--back .house-art { left: 685px; top: 73px; width: 160px; height: 88px; }

  .tape {
    position: absolute;
    background: linear-gradient(180deg, var(--tape-yellow), var(--tape-dark));
  }
  .tape--horizontal { left: 248px; top: 248px; width: 694px; height: 42px; }
  .tape--vertical { left: 70px; top: 0; width: 44px; height: 443px;
    background: linear-gradient(90deg, var(--tape-yellow), var(--tape-dark)); }

  .constructors {
    position: absolute; left: 243px; top: 296px;
    font-size: 66px; color: var(--constructors-grey); letter-spacing: 1px;
  }

  .rule { position: absolute; left: 130px; right: 0; height: 1px; background: var(--rule-olive); }
  .rule--top { top: 216px; }
  .rule--bottom { top: 366px; left: 133px; }

  .person-name { position: absolute; left: 125px; top: 237px; font-size: 26px; color: var(--mint-text); }
  .person-role { position: absolute; left: 130px; top: 276px; font-size: 28px; color: var(--white); }
  .website { position: absolute; left: 133px; top: 322px; font-size: 17px; color: var(--web-yellow); }

  .contact { position: absolute; display: flex; align-items: center; gap: 8px; color: var(--mint-text); }
  .contact svg { flex: none; }
  .contact--phone { left: 503px; top: 234px; font-size: 28px; }
  .contact--address { left: 500px; top: 283px; font-size: 17px; }
  .contact--email { left: 501px; top: 321px; font-size: 14px; }

  .slogan {
    position: absolute; left: 0; width: 980px; top: 392px; text-align: center;
    font-size: 22px; letter-spacing: 2px; word-spacing: 10px; color: var(--white);
  }
</style>
</head>
<body>
<main class="sheet">

  <section class="card card--front" aria-label="Card front">
    <div class="brand-name">Vorel</div>
    <div class="house-art" role="img" aria-label="Sketched cartoon house illustration"></div>
    <div class="tape tape--horizontal" role="img" aria-label="Extended yellow measuring tape illustration"></div>
    <div class="constructors">CONSTRUCTORS</div>
  </section>
  <div class="side-label side-label--front">FRONT</div>

  <section class="card card--back" aria-label="Card back">
    <div class="tape tape--vertical" role="img" aria-label="Vertical yellow measuring tape illustration"></div>
    <div class="brand-name">Vorel</div>
    <div class="house-art" role="img" aria-label="Sketched cartoon house illustration"></div>

    <div class="rule rule--top"></div>
    <div class="person-name">MR DINESH MALARKODIYAN</div>
    <div class="person-role">DIRECTOR</div>
    <div class="website">VORELCONSTRUCTIONS.EXAMPLE.COM.AU</div>

    <div class="contact contact--phone">
      <svg width="20" height="30" viewBox="0 0 20 30" aria-hidden="true">
        <rect x="2" y="3" width="16" height="26" rx="3" fill="none" stroke="#3ee8dc" stroke-width="2.5"/>
        <rect x="5" y="7" width="10" height="7" fill="#3ee8dc"/>
        <g fill="#3ee8dc"><circle cx="6.5" cy="18" r="1.3"/><circle cx="10" cy="18" r="1.3"/><circle cx="13.5" cy="18" r="1.3"/>
        <circle cx="6.5" cy="22" r="1.3"/><circle cx="10" cy="22" r="1.3"/><circle cx="13.5" cy="22" r="1.3"/></g>
        <rect x="14" y="0" width="2.5" height="4" fill="#3ee8dc"/>
      </svg>
      <span>0417305862</span>
    </div>
    <div class="contact contact--address">
      <svg width="30" height="26" viewBox="0 0 30 26" aria-hidden="true">
        <path d="M15 1 L29 13 H25 V25 H18 V17 H12 V25 H5 V13 H1 Z" fill="#3ee8dc"/>
      </svg>
      <span>8/3 FENWICK LANE CARROWMERE VIC 3990</span>
    </div>
    <div class="contact contact--email">
      <svg width="30" height="30" viewBox="0 0 30 30" aria-hidden="true">
        <text x="15" y="24" text-anchor="middle" font-size="30" font-family="Questrial, sans-serif" fill="#3ee8dc">@</text>
      </svg>
      <span>TMELO@VORELCONSTRUCTIONS.EXAMPLE.COM.AU</span>
    </div>
    <div class="rule rule--bottom"></div>

    <div class="slogan">“CONSTRUCTION YOU CAN COUNT ON”</div>
  </section>
  <div class="side-label side-label--back">BACK</div>

</main>
</body>
</html>
```